Wordpress Design for Dads Weightloss membership site

BrisketPopsHall.com

Key points
Its for Dads - so please try and make this appeal to Dad
Its for overweight men
Its a Dojo - i.e. a training school for Dads to lose weight and progress. think Karate school.

I will be launching a site to support and help Overweight Dads lose the fat. Target market is Dads 30 years + in North America, Europe.
The audience is probably well overweight but struggle to find the time due to the challenges of a demanding job and family.

The site will be a no nonsense holistic approach on how to change your lifestyle through walking/Running/Crossfit and adopting the Paleo diet. I am a 42 year old with 4 children under 7, with a demanding job in IT sales working for a global corporate. I will share my journey as a blog initially but have the intention to turn this into a business via a membership site / coaching.

I want this to be a fun yet educational but slightly tongue in cheek. Cartoon style is fine, bold and fresh. I expect a large number of users to be viewing this on their iPads or other mobile devices so please bare this in mind.

I do not want this looking like the conventional Personal Trainer web site. This looks too clinical. I am not in perfect shape myself but have proven my methods work, I am still on the journey, so want this site to be something my audience can identify with - ie I am not much different then them.

Summary
I am accepting designs concepts for my personal blog and web presence – http://www.BrisketPopsHall. The Blog, subtitled “Grit and Gut Reset for Pops”, will provide a platform upon which I wish to build a personal brand and market myself ultimately as a 1:many coach.

The successful design will balance an professional design with a bit of humour and be attractive to a male audience. The theme MUST match the concept of a oriental martial arts school. Use of Japanese imagery such as Pagodas,Zen, Bushido and Samurai is encouraged. The Web Header (Standard Header) MUST include the title and sub title and include graphics to depict a Dojo. I am open to the style and colors to be used but again please look for influences from the Far East

Technical Requirements
The design must be implementable in WordPress using “Standard Theme” Customizations to Standard Theme are allowed, but should not be extraordinary.

The design must be implementable using clean and standard html/css techniques.

The design must include a standard header that uses the Title and subtitle as discussed above. This is the key element of the design and should be your prime focus.

The design must include placeholders for advertisements on each page. Banner ad horizontal. Banner ad tower in the right .

The design must include a standard site template/shell and at least 3 internal page designs.

Designs should be submitted for (at minimum) the following pages
Home
About
Video Blog – a video surrounded by
Podcast
Primary Navigation / Pages

The Home page should include an area for Email Optin in the top right corner.
The About Page to also include the Email Optin
Each blog post should contain social actions – the ability to tweet, share, etc. . .with the click of a button.

In addition to the core content, the home page should provide a brief introduction and video.

Standard Page template to include
. This page will serve as a template for all other “standard” pages. Please include the basic elements for a website in this page. These should include:
• A minimum of 3 Headings - H1, H2, and H3
• A bulleted list
• A numbered list
• A table
• An image
• A call to action (typically an image/button)

to the public or not.

Contact
No need for a separate layout unless desired.

Other Elements
The Blog should provide quick access to the following blog “categories”:
Primal/Paleo Nutrition
Paleo Recipes
Family/Work Balance
Reducing Stress
Career Hacking
Faith and Family

The template should include prominent links to each of my social media pages:
Twitter
LinkedIn
YouTube
Facebook
Google+
PinQuilt

The template should include a link to the blog archives

Target Market(s)

English Speaking , Male, 30+, Father, all demographics

Industry/Entity Type

Training

Requirements
Must have
• Optin area for email address on sidebar
Social icons for Pinquilt, Facebook, You tube
Privacy, About, Terms and Conditions Navigation
Blog area
Members login - small subtle top right
First Time Visitor start Here
Nice to have
• Japanese Dojo feel to it
Should not have
• Try not to look like the many other Personal training / coaching web sites. Want to stand out from the crowd. Although this is initially a blog it will become my business. So branding is important - but in a male, not overly serious way.

```html
<!DOCTYPE html>
<html lang="en">
<head>
<meta charset="utf-8">
<title>Brisket Pops Hall</title>
<link href="https://fonts.googleapis.com/css2?family=PT+Sans:wght@400;700&family=Open+Sans:wght@300;400&display=swap" rel="stylesheet">
<style>
:root{
  --red:#e01f2a;
  --dark:#3a3a3a;
  --darker:#2c2c2c;
  --ink:#333;
  --muted:#777;
  --line:#d6d6d6;
  --panel:#ededed;
  --page:#f7f7f7;
  --wood:#8a4f2a;
  --wood-light:#b57444;
}
*{box-sizing:border-box;margin:0;padding:0}
html,body{width:1103px;height:1200px;overflow:hidden}
body{position:relative;background:var(--page);font-family:"PT Sans",sans-serif;color:var(--ink)}
.abs{position:absolute}
a{color:inherit}

/* header */
.topline{left:0;top:0;width:1103px;height:7px;background:#222}
.header{left:0;top:7px;width:1103px;height:135px;background:linear-gradient(#fdfdfd,#ececec)}
.login{left:919px;top:0;width:83px;height:28px;background:linear-gradient(#555,#2e2e2e);color:#fff;font-size:13px;text-align:center;line-height:28px;border-radius:0 0 4px 4px}
.brand{left:127px;top:40px;width:178px;height:84px;border:1px solid #bbb;background:#fff;display:flex;align-items:center;justify-content:center;gap:8px}
.brand-name{font-weight:700;color:var(--red);font-size:21px;line-height:1.05;text-align:left}
.brand-dot{width:16px;height:16px;border-radius:50%;background:var(--red);flex:none}
.connect{left:721px;top:44px;font-size:20px;color:#222}
.connect i{font-family:"Open Sans",sans-serif;font-weight:300}
.connect b{font-weight:700}
.social{left:894px;top:44px;display:flex;gap:5px}
.social span{width:22px;height:22px;border-radius:50%;background:linear-gradient(#6a8fc4,#2d5a9c)}
.social span:nth-child(1){background:linear-gradient(#7dd3f5,#2aa3db)}
.social span:nth-child(3){background:linear-gradient(#f7a04a,#d9601a)}
.social span:nth-child(4){background:linear-gradient(#4fa0d6,#1d6aa8)}
.optin{left:714px;top:81px;width:288px;height:41px;border:1px solid var(--line);border-radius:4px;background:#f8f8f8}
.optin svg{position:absolute;left:12px;top:6px}
.optin .field{position:absolute;left:62px;top:10px;width:154px;height:22px;border:1px solid #ccc;background:#fff;font-size:11px;color:#888;padding:3px 10px}
.optin .go{position:absolute;left:221px;top:11px;width:46px;height:18px;border-radius:4px;background:linear-gradient(#f24a52,#c5121b);color:#fff;font-size:12px;font-weight:700;text-align:center;line-height:18px}

/* nav */
.nav{left:0;top:142px;width:1103px;height:42px;background:linear-gradient(#4a4a4a,#333)}
.nav-item{top:14px;color:#fff;font-size:13px}
.nav-home{left:111px;top:6px;width:72px;height:29px;background:linear-gradient(#fff,#e4e4e4);border-radius:3px;color:#222;font-weight:700;text-align:center;line-height:29px}
.search{left:813px;top:9px;width:181px;height:23px;border-radius:12px;background:#fff;font-size:11px;color:#aaa;font-style:italic;padding:5px 13px;overflow:hidden}
.search b{position:absolute;right:0;top:0;width:28px;height:23px;background:linear-gradient(#8cc63f,#5a9e1c)}
.search svg{position:absolute;right:8px;top:6px}

/* hero */
.hero-photo{left:101px;top:184px;width:669px;height:275px;background:linear-gradient(180deg,var(--wood) 0%,var(--wood-light) 45%,#e9e3da 65%,#c6b49a 100%)}
.hero-side{left:770px;top:184px;width:232px;height:275px;background:#fff;border:1px solid var(--line);border-left:0}
.dojo-mark{left:16px;top:44px;width:188px;height:80px;border:1px solid #bbb;display:flex;align-items:center;justify-content:center;gap:8px}
.dojo-mark span{font-weight:700;color:#222;font-size:19px}
.dojo-mark i{width:14px;height:14px;border-radius:50%;background:var(--red)}
.hero-copy{left:16px;top:154px;width:206px;font-size:10.5px;line-height:13px;color:#333}
.cta-bar{left:101px;top:459px;width:901px;height:49px;background:linear-gradient(#4a4a4a,#2e2e2e);border:1px solid #222}
.cta-bar .lead{left:7px;top:12px;color:#fff;font-size:20px;font-family:"Open Sans",sans-serif;font-weight:300}
.cta-bar .tag{left:211px;top:13px;color:#fff;font-size:18px;font-family:"Open Sans",sans-serif;font-weight:300}
.cta-bar svg.chev{position:absolute;left:176px;top:3px}
.call{left:713px;top:6px;width:151px;height:36px;border-radius:4px;background:linear-gradient(#fff,#e2e2e2);color:var(--red);font-size:19px;font-family:"Open Sans",sans-serif;line-height:36px;padding-left:52px}
.call svg{position:absolute;left:12px;top:7px}

/* welcome */
.welcome-title{left:106px;top:532px;font-family:"Open Sans",sans-serif;font-weight:300;font-size:29px;color:#222}
.welcome-title em,.news-title em{font-style:normal;color:var(--red)}
.welcome-copy{left:106px;top:578px;width:610px;font-family:"Open Sans",sans-serif;font-weight:300;font-size:11.8px;line-height:21px;color:#444}
.btn-more{left:105px;top:698px;width:91px;height:27px;border-radius:3px;background:linear-gradient(#6a6a6a,#3e3e3e);color:#fff;font-size:11.5px;text-align:center;line-height:27px;box-shadow:0 4px 5px rgba(0,0,0,.12)}

/* video */
.video{left:738px;top:535px;width:264px;height:198px;border:2px solid #555;border-radius:3px;background:linear-gradient(90deg,#cfcdc6,#e6e4df 50%,#bdb9b1)}
.video .play{position:absolute;left:112px;top:68px;width:42px;height:42px;border-radius:50%;background:rgba(30,30,30,.85)}
.video .play svg{position:absolute;left:15px;top:12px}
.video .tools{position:absolute;right:4px;top:4px;display:flex;flex-direction:column;gap:4px}
.video .tools span{width:26px;height:20px;background:#333;border-radius:3px}
.video .bar{position:absolute;left:0;bottom:0;width:100%;height:22px;background:#1d1d1d;color:#ddd;font-size:8px;font-weight:700;padding:10px 0 0 104px}
.video .bar::before{content:"";position:absolute;left:0;top:0;width:130px;height:5px;background:#d01818}
.video .bar::after{content:"";position:absolute;left:130px;top:0;right:0;height:5px;background:#e7a9a9}
.video .hd{position:absolute;right:10px;bottom:3px;color:#ddd;font-size:8px;font-weight:700}

/* gallery */
.gallery{left:101px;top:762px;width:615px;height:165px;background:linear-gradient(#e8e8e8,#f2f2f2);border-radius:6px;box-shadow:0 2px 2px rgba(0,0,0,.08)}
.thumb{top:19px;width:111px;height:103px;background:#fff;border:1px solid #ddd;padding:3px}
.thumb div{width:100%;height:100%}
.thumb-cap{top:129px;font-size:10.5px;color:#333}

/* news */
.news-title{left:106px;top:952px;font-family:"Open Sans",sans-serif;font-weight:300;font-size:29px;color:#222}
.news-photo{left:101px;top:1001px;width:113px;height:104px;background:#fff;border:1px solid #ddd;padding:4px}
.news-photo div{width:100%;height:100%;background:linear-gradient(#4a4a4a,#9a8f80 60%,#c9c2b6)}
.news-date{left:225px;top:1003px;font-size:12.5px;color:var(--red)}
.news-copy{left:225px;top:1023px;width:380px;font-size:11px;line-height:16.5px;color:#333;text-decoration:underline}
.news-copy em{font-style:normal;color:var(--red)}
.news-more{left:225px;top:1078px;font-size:11px;text-decoration:underline;color:#222}

/* blog */
.blog{left:739px;top:753px;width:263px;height:372px;border:1px solid var(--line);background:#f4f4f4}
.blog-head{position:absolute;left:0;top:0;width:100%;height:49px;background:linear-gradient(#575757,#2f2f2f);color:#fff;font-family:"Open Sans",sans-serif;font-size:20px;padding:12px 0 0 48px}
.blog-head svg{position:absolute;left:10px;top:9px}
.cats{position:absolute;left:0;top:49px;width:100%;height:36px;background:#fff;font-size:9.5px;color:#444;display:flex;gap:11px;padding:18px 0 0 9px;border-bottom:1px solid #ddd}
.cats span{text-decoration:underline}
.post{position:absolute;left:0;width:100%;height:65px;border-bottom:1px solid #e0e0e0;padding:8px 0 0 16px}
.post h4{font-size:12.5px;font-weight:400;color:#222}
.post h4::before{content:"";position:absolute;left:7px;top:12px;border:4px solid transparent;border-left:5px solid #333}
.post p{font-size:10px;line-height:13px;color:#888;width:232px}
.post .share{position:absolute;right:12px;bottom:6px;font-size:10px;color:#444;display:flex;gap:4px;align-items:center}
.post .share i{width:14px;height:14px;border-radius:2px;background:#3b5b99}
.post .share i+i{background:#41a6e0}
.blog-more{position:absolute;left:17px;bottom:7px;font-size:10.5px;text-decoration:underline;color:#222}

/* footer */
.footer{left:0;top:1141px;width:1103px;height:59px;background:#3c3c3c;color:#ddd;font-size:11px;text-align:center;line-height:59px}
</style>
</head>
<body>

<div class="abs topline"></div>
<header class="abs header"></header>
<div class="abs login">Login</div>

<div class="abs brand">
  <span class="brand-dot"></span>
  <span class="brand-name">BRISKET<br>POPS HALL</span>
</div>

<div class="abs connect"><i>let’s stay</i> <b>Connected!</b></div>
<div class="abs social" aria-label="Social links"><span></span><span></span><span></span><span></span></div>

<div class="abs optin">
  <svg width="40" height="32" viewBox="0 0 40 32"><rect x="6" y="4" width="24" height="26" rx="2" fill="#fff" stroke="#bbb" transform="rotate(-12 18 17)"/><path d="M14 17l5 6 10-14" fill="none" stroke="#d9a321" stroke-width="3" stroke-linecap="round"/></svg>
  <div class="field">Email:</div>
  <div class="go">Go</div>
</div>

<nav class="abs nav">
  <div class="abs nav-home">Home</div>
  <div class="abs nav-item" style="left:239px">About</div>
  <div class="abs nav-item" style="left:347px">Video Blog – a video surrounded by</div>
  <div class="abs nav-item" style="left:606px">Podcast</div>
  <div class="abs search">search...<b></b><svg width="11" height="11" viewBox="0 0 11 11"><circle cx="4.5" cy="4.5" r="3.2" fill="none" stroke="#fff" stroke-width="1.6"/><path d="M7 7l3 3" stroke="#fff" stroke-width="1.8"/></svg></div>
</nav>

<div class="abs hero-photo" role="img" aria-label="Group photo of karate students in white uniforms in a wooden dojo"></div>
<aside class="abs hero-side">
  <div class="abs dojo-mark"><i></i><span>Kestrel Hall</span></div>
  <p class="abs hero-copy">Lorem Ipsum is simply dummy text of the printing and typesetting industry. Lorem Ipsum has been the industry's standard dummy text ever since the 1500s, when an unknown printer took a galley of type and scrambled it to make a type specimen book. It has survived not only five centuries, but also the leap into</p>
</aside>

<section class="abs cta-bar">
  <div class="abs lead">Ready to Get Fit?</div>
  <svg class="chev" width="20" height="44" viewBox="0 0 20 44"><path d="M3 2l12 20-12 20" fill="none" stroke="#e01f2a" stroke-width="2"/></svg>
  <div class="abs tag">Let Brisket Pops Hall help you get in best shape of your life!</div>
  <div class="abs call">
    <svg width="32" height="22" viewBox="0 0 32 22"><rect x="2" y="6" width="26" height="14" rx="3" fill="#8fb0d6" stroke="#4d6f9a"/><path d="M5 7q10-9 20 0" fill="none" stroke="#4d6f9a" stroke-width="3"/><rect x="9" y="10" width="12" height="7" fill="#fff"/></svg>
    Call Now !
  </div>
</section>

<h1 class="abs welcome-title">Welcome to <em>Brisket Pops Hall</em></h1>
<p class="abs welcome-copy">Lorem Ipsum is simply dummy text of the printing and typesetting industry. Lorem Ipsum has been the industry's standard dummy text ever since the 1500s, when an unknown printer took a galley of type and scrambled it to make a type specimen book. It has survived not only five centuries, but also the leap into electronic typesetting, remaining essentially unchanged. It was popularised in the 1960s with the release of Tessaprint sheets containing Lorem Ipsum passages, and more etc.</p>
<div class="abs btn-more">Read More</div>

<div class="abs video" role="img" aria-label="Video of two martial artists training in a dojo">
  <div class="tools"><span></span><span></span><span></span><span></span></div>
  <div class="play"><svg width="14" height="18" viewBox="0 0 14 18"><path d="M0 0l14 9-14 9z" fill="#fff"/></svg></div>
  <div class="bar">1:20 / 2:50</div>
  <div class="hd">HD</div>
</div>

<section class="abs gallery">
  <div class="abs thumb" style="left:14px"><div role="img" aria-label="Student with a wooden staff by the sea" style="background:linear-gradient(#9ab0c4,#d8d8d2 60%,#b8ad98)"></div></div>
  <div class="abs thumb" style="left:133px"><div role="img" aria-label="Instructor in white uniform with black belt" style="background:linear-gradient(#2a2a2a,#6d6d6d 50%,#e8e8e8)"></div></div>
  <div class="abs thumb" style="left:252px"><div role="img" aria-label="Close-up of a karate uniform and black belt" style="background:linear-gradient(90deg,#1a1a1a,#f2f2f2 45%,#dcdcdc)"></div></div>
  <div class="abs thumb" style="left:371px"><div role="img" aria-label="Two students sparring on blue and red mats" style="background:linear-gradient(#35599c,#8fa6cf 55%,#c23a3a)"></div></div>
  <div class="abs thumb" style="left:490px"><div role="img" aria-label="Students practising kata" style="background:linear-gradient(#c8a98a,#efe8e0 60%,#d6cbbd)"></div></div>
  <span class="abs thumb-cap" style="left:17px">Lorem Ipsum</span>
  <span class="abs thumb-cap" style="left:137px">dummy text</span>
  <span class="abs thumb-cap" style="left:254px">Lorem Ipsum</span>
  <span class="abs thumb-cap" style="left:374px">dummy text</span>
  <span class="abs thumb-cap" style="left:493px">Lorem Ipsum</span>
</section>

<h2 class="abs news-title">Our <em>News</em></h2>
<div class="abs news-photo"><div role="img" aria-label="Two students practising with wooden swords"></div></div>
<div class="abs news-date">Sat, Jul 19,2009</div>
<p class="abs news-copy">Lorem Ipsum is simply dummy text of the printing and typesetting industry. Lorem Ipsum has been the industry's standard dummy text ever since the 1500s, when an unknown printer took a <em>galley of type</em> and scrambled it to make a type</p>
<a class="abs news-more">Read More News</a>

<aside class="abs blog">
  <div class="blog-head">
    <svg width="30" height="30" viewBox="0 0 30 30"><rect x="4" y="3" width="18" height="24" rx="1" fill="#f4f4f4" stroke="#999"/><path d="M8 9h10M8 13h10M8 17h7" stroke="#9ab" stroke-width="1.4"/><path d="M16 26l10-14 2 2-10 14-3 1z" fill="#5d8fc4"/></svg>
    Our Blog
  </div>
  <div class="cats"><span>Primal</span><span>Paleo</span><span>Family</span><span>Career Hacking</span><span>Faith and Family</span></div>
  <div class="post" style="top:86px"><h4>JUL 18, 2011</h4><p>Lorem Ipsum is simply dummy text of the printing and typesetting industry.</p><div class="share">Share <i></i><i></i></div></div>
  <div class="post" style="top:154px"><h4>JUL 18, 2011</h4><p>Lorem Ipsum is simply dummy text of the printing and typesetting industry.</p><div class="share">Share <i></i><i></i></div></div>
  <div class="post" style="top:219px"><h4>JUL 18, 2011</h4><p>Lorem Ipsum is simply dummy text of the printing and typesetting industry.</p><div class="share">Share <i></i><i></i></div></div>
  <div class="post" style="top:284px"><h4>JUL 18, 2011</h4><p>Lorem Ipsum is simply dummy text of the printing and typesetting industry.</p><div class="share">Share <i></i><i></i></div></div>
  <a class="blog-more">Read More Posts ▸▸</a>
</aside>

<footer class="abs footer">COPYRIGHT - include a copyright statement © 2012 BrisketPopsHall | All rights reserved.</footer>

</body>
</html>
```